furniture and home contents restoration

I need to list the services that we perform in our studio.
we serve the general public as well as the insurance/ remediation industry

```html
<!DOCTYPE html>
<html lang="en">
<head>
<meta charset="utf-8">
<title>Calderwick Workshop – Business Card</title>
<link href="https://fonts.googleapis.com/css2?family=Source+Sans+3:wght@400;600;700;800&display=swap" rel="stylesheet">
<style>
  :root {
    --page: #e4e4e5;
    --ink: #1f2b33;
    --card-light: #ececed;
    --text-light: #eef1f3;
    --text-grey: #6d6f72;
    --swoosh-grey: #8e8f92;
    --rule: #9a9c9f;
    --bullet: #c3c8cc;
  }
  * { margin: 0; padding: 0; box-sizing: border-box; }
  html, body { width: 1200px; height: 1200px; overflow: hidden; }
  body {
    background: var(--page);
    font-family: "Source Sans 3", sans-serif;
    position: relative;
  }
  .card {
    position: absolute;
    left: 263px;
    width: 683px;
    height: 390px;
    border-radius: 34px;
    overflow: hidden;
  }
  .card--back { top: 165px; background: var(--ink); color: var(--text-light); }
  .card--front { top: 654px; background: var(--card-light); color: var(--text-grey); }

  /* services list */
  .services {
    position: absolute;
    top: 88px;
    list-style: none;
    font-size: 15.5px;
    line-height: 19.6px;
  }
  .services--left { left: 48px; }
  .services--right { left: 351px; }
  .services li { position: relative; padding-left: 21px; white-space: nowrap; }
  .services li::before {
    content: "";
    position: absolute;
    left: 1px; top: 7px;
    width: 11px; height: 5px;
    border-radius: 3px;
    background: var(--bullet);
  }
  .services li::after {
    content: "";
    position: absolute;
    left: 10px; top: 5.5px;
    border-left: 5px solid var(--bullet);
    border-top: 4px solid transparent;
    border-bottom: 4px solid transparent;
  }
  .assessment {
    position: absolute;
    left: 0; right: 0; top: 321px;
    text-align: center;
    font-size: 15.5px;
    line-height: 20px;
  }
  .assessment strong { font-weight: 700; }

  /* front */
  .brand {
    position: absolute;
    right: 346px;
    top: 133px;
    text-align: right;
    color: var(--ink);
    font-weight: 800;
    font-size: 41px;
    line-height: 40px;
    letter-spacing: 0.2px;
    white-space: nowrap;
  }
  .brand-tagline {
    position: absolute;
    left: 120px; width: 200px;
    top: 232px;
    text-align: center;
    font-size: 15.5px;
  }
  .divider {
    position: absolute;
    left: 360px; top: 123px;
    width: 1px; height: 155px;
    background: var(--rule);
  }
  .contact { position: absolute; left: 386px; top: 119px; }
  .contact-name {
    color: var(--ink);
    font-weight: 700;
    font-size: 20.5px;
    line-height: 26px;
    margin-bottom: 7px;
  }
  .contact-address { font-size: 15.5px; line-height: 20px; margin-bottom: 3px; }
  .contact-lines { list-style: none; font-size: 15.5px; line-height: 19.6px; }
  .contact-lines li { display: flex; align-items: center; }
  .contact-lines svg { width: 12px; height: 12px; margin-right: 10px; fill: var(--ink); flex: none; }
  .footer-band { position: absolute; left: 0; bottom: 0; width: 683px; height: 390px; }
  .footer-text {
    position: absolute;
    right: 52px; top: 337px;
    text-align: right;
    color: var(--text-light);
    font-size: 15.5px;
    line-height: 20px;
  }
</style>
</head>
<body>

<section class="card card--back">
  <ul class="services services--left">
    <li>Antique Repair and Restoration</li>
    <li>Art Cleaning and Remounting</li>
    <li>Art and Mirror Frame Repair</li>
    <li>Chandelier Cleaning and Restoration</li>
    <li>Document Restoration</li>
    <li>Glass, Ceramic and Mirror Repair</li>
    <li>Hardware Repair and Restoration</li>
    <li>Kitchen Removal and Reinstallation</li>
    <li>Lamp Cleaning and Restoration</li>
    <li>Lamp Shade Replacement</li>
  </ul>
  <ul class="services services--right">
    <li>Metal Polishing and Restoration</li>
    <li>Odor Removal and Ozone Services</li>
    <li>Photo Restoration</li>
    <li>Upholstery Cleaning and Deodorizing</li>
    <li>In-House Upholstery and Reupholstery</li>
    <li>Rug Cleaning and Restoration</li>
    <li>Musical Instrument Restoration</li>
    <li>Window Treatment Repair/ Restoration</li>
    <li>Leather Restoration and Replacement</li>
    <li>Piano Restoration and Repair</li>
  </ul>
  <p class="assessment">
    <strong>On-Site Inspections and Desk Review Services</strong><br>
    Assessment Reports and Estimates for Repair and Restoration
  </p>
</section>

<section class="card card--front">
  <svg class="footer-band" viewBox="0 0 683 390" aria-hidden="true">
    <path d="M0 365 Q 200 326 500 326 L500 328 Q 220 334 104 390 L0 390 Z" fill="var(--swoosh-grey)"/>
    <path d="M108 390 Q 210 336 490 331 L683 331 L683 390 Z" fill="var(--ink)"/>
  </svg>

  <div class="brand">CALDERWICK<br>Workshop</div>
  <p class="brand-tagline">Home Contents Restoration</p>
  <div class="divider"></div>

  <div class="contact">
    <p class="contact-name">Daniel Ferrante</p>
    <p class="contact-address">128 Orchard Hill Rd.<br>Riverton, NY 10590</p>
    <ul class="contact-lines">
      <li><svg viewBox="0 0 12 12"><path d="M2.5 0.5 L4.5 0.5 L5.2 3.2 L3.8 4.3 Q4.8 6.8 7.7 8.2 L8.8 6.8 L11.5 7.5 L11.5 9.5 Q11.5 11.5 9.5 11.5 Q0.5 10.5 0.5 2.5 Q0.5 0.5 2.5 0.5Z"/></svg>555.210.4800</li>
      <li><svg viewBox="0 0 12 12"><path d="M3 0 H9 Q10 0 10 1 V11 Q10 12 9 12 H3 Q2 12 2 11 V1 Q2 0 3 0Z M3.3 1.5 V9.5 H8.7 V1.5Z"/></svg>555.318.2957</li>
      <li><svg viewBox="0 0 12 12"><path d="M3 0 H9 V3 H3Z M1 4 H11 Q12 4 12 5 V9 H10 V12 H2 V9 H0 V5 Q0 4 1 4Z M3 8 V11 H9 V8Z"/></svg>555.210.4815</li>
      <li><svg viewBox="0 0 12 12"><path d="M0 2.5 H12 L6 7Z M0 3.8 L6 8.3 L12 3.8 V10 H0Z"/></svg>cwshop@mailbox.com</li>
    </ul>
  </div>

  <p class="footer-text">Serving The General Public<br>and The Insurance Industry for Over 40 Years</p>
</section>

</body>
</html>
```